Silver Reed Signage

Please I'm looking to have signage for business front door and 2 windows. Wow me! It is the first thing ppl will see always.
I'm looking to have some privacy because I am in the beauty business, so privacy is key. Please look at attached pictures of front and windows. Make it elegant because the spa shop is all about luxury excellence. I need website, Email address phone number in name of the company. I'd like to also put some services somewhere on the signage (s) you can place it where you'd think it would be best. Lymphatic Drainage, Body Sculpting/contouring, Detoxing, Cavitation, Facials ..... and much more

```html
<!DOCTYPE html>
<html lang="en">
<head>
<meta charset="utf-8">
<title>Silver Reed Signage</title>
<link rel="stylesheet" href="https://fonts.googleapis.com/css2?family=Cinzel:wght@500;600;700&family=Marcellus&family=Montserrat:wght@500;600&display=swap">
<style>
  :root {
    --backdrop: #2b2b2b;
    --storefront: #3b3c3e;
    --frame: #1d1e20;
    --violet: #6f6cb2;
    --violet-soft: #7c79bb;
    --violet-bright: #5a22e6;
    --violet-deep: #2a2488;
    --sea-green: #55b08f;
    --sea-green-soft: #62b998;
    --panel-white: #ffffff;
    --ink: #1b1b1b;
    --photo-light: #e2e3e4;
    --photo-mid: #c4c6c8;
  }
  * { margin: 0; padding: 0; box-sizing: border-box; }
  html, body { width: 1200px; height: 1200px; overflow: hidden; background: var(--backdrop); }
  .canvas { position: relative; width: 1200px; height: 1200px; }

  /* Storefront window set */
  .storefront {
    position: absolute; left: 44px; top: 418px; width: 520px; height: 462px;
    background: var(--storefront);
    border-top: 6px solid var(--frame);
  }
  .window-tall {
    position: absolute; left: 62px; top: 426px; width: 150px; height: 440px;
    background: var(--sea-green); overflow: hidden;
    outline: 7px solid var(--frame);
  }
  .window-tall .word {
    position: absolute; left: 75px; top: 24px;
    writing-mode: vertical-rl;
    font-family: "Marcellus", serif; font-size: 72px; letter-spacing: 6px;
    color: var(--panel-white); line-height: 1;
    transform: translateX(-50%);
  }
  .window-tall .photo {
    position: absolute; left: 0; bottom: 0; width: 100%; height: 152px;
    background: linear-gradient(175deg, #e9e4df 0%, #caa083 35%, #a8704e 70%, #8a5a40 100%);
  }
  .window-tall svg.wave { position: absolute; left: 0; top: 276px; }

  .window-wide {
    position: absolute; left: 226px; top: 450px; width: 318px; height: 162px;
    background: var(--violet); overflow: hidden;
    outline: 7px solid var(--frame);
  }
  .window-wide .mark {
    position: absolute; left: 14px; top: 36px; width: 90px; height: 90px;
    border-radius: 50%; background: var(--panel-white);
  }
  .window-wide .word {
    position: absolute; left: 124px; top: 54px;
    font-family: "Marcellus", serif; font-size: 54px; letter-spacing: 1px;
    color: var(--panel-white); line-height: 1;
  }

  /* Door panel */
  .door {
    position: absolute; left: 646px; top: 104px; width: 496px; height: 992px;
    background: var(--panel-white); overflow: hidden;
  }
  .door .photo {
    position: absolute; left: 0; top: 0; width: 100%; height: 420px;
    background: linear-gradient(100deg, var(--photo-mid) 0%, var(--photo-light) 30%, #d8c4b4 50%, var(--photo-light) 72%, var(--photo-mid) 100%);
  }
  .door svg.wave { position: absolute; left: 0; top: 340px; }

  .service {
    position: absolute; display: flex; align-items: flex-start; gap: 4px;
    font-family: "Cinzel", serif; font-weight: 700; font-size: 25px;
    line-height: 0.96; color: var(--sea-green); letter-spacing: -0.6px;
  }
  .service svg { flex: none; margin-top: 3px; }
  .s-lymph { left: 26px; top: 426px; }
  .s-sculpt { left: 212px; top: 426px; }
  .s-maint { left: 26px; top: 488px; }
  .s-cavit { left: 259px; top: 492px; }
  .s-facial { left: 259px; top: 536px; }
  .s-detox { left: 157px; top: 576px; }

  .brand-dot {
    position: absolute; left: 208px; top: 660px; width: 80px; height: 80px;
    border-radius: 50%; background: var(--violet-bright);
  }
  .brand-name {
    position: absolute; left: 0; top: 800px; width: 100%; text-align: center;
    font-family: "Montserrat", sans-serif; font-weight: 500; font-size: 48px;
    color: var(--violet-bright); line-height: 1; letter-spacing: 0.5px;
  }
  .tagline {
    position: absolute; left: 0; top: 852px; width: 100%; text-align: center;
    font-family: "Montserrat", sans-serif; font-weight: 500; font-size: 11.5px;
    letter-spacing: 1.6px; color: var(--violet-deep);
  }
  .phone {
    position: absolute; left: 0; top: 872px; width: 100%;
    display: flex; justify-content: center; align-items: center; gap: 6px;
    font-family: "Cinzel", serif; font-weight: 500; font-size: 58px; line-height: 1;
    color: var(--sea-green);
  }
  .web {
    position: absolute; left: 0; top: 930px; width: 100%; text-align: center;
    font-family: "Cinzel", serif; font-weight: 500; font-size: 25px; color: var(--ink); line-height: 1;
  }
  .web .domain { color: var(--violet-deep); }
  .email {
    position: absolute; left: 0; top: 962px; width: 100%; text-align: center;
    font-family: "Cinzel", serif; font-weight: 600; font-size: 16px; color: var(--violet); line-height: 1;
  }
</style>
</head>
<body>
<main class="canvas">

  <div class="storefront"></div>

  <section class="window-tall">
    <span class="word">REED</span>
    <svg class="wave" width="150" height="20" viewBox="0 0 150 20" aria-hidden="true">
      <path d="M0 14 C40 2 100 0 150 6 L150 20 L0 20 Z" fill="#e9e4df"/>
    </svg>
    <div class="photo" role="img" aria-label="Photo of a smiling woman receiving a facial massage"></div>
  </section>

  <section class="window-wide">
    <div class="mark"></div>
    <span class="word">SILVER</span>
  </section>

  <section class="door">
    <div class="photo" role="img" aria-label="Photo of a slim woman in white sportswear measuring her waist with a tape measure"></div>
    <svg class="wave" width="496" height="110" viewBox="0 0 496 110" aria-hidden="true">
      <path d="M0 40 C60 20 120 18 200 38 C300 62 420 40 496 0 L496 110 L0 110 Z" fill="#6f6cb2"/>
      <path d="M0 56 C60 34 120 32 200 52 C300 76 420 54 496 12 L496 110 L0 110 Z" fill="#ffffff"/>
    </svg>

    <div class="service s-lymph"><svg width="18" height="18" viewBox="0 0 18 18"><circle cx="9" cy="9" r="7.5" fill="none" stroke="#6f6cb2" stroke-width="1.6"/><path d="M5.5 9.2 L8 11.6 L13 6.2" fill="none" stroke="#6f6cb2" stroke-width="1.8"/></svg><span>Lymphatic<br>Drainage</span></div>
    <div class="service s-sculpt"><svg width="18" height="18" viewBox="0 0 18 18"><circle cx="9" cy="9" r="7.5" fill="none" stroke="#6f6cb2" stroke-width="1.6"/><path d="M5.5 9.2 L8 11.6 L13 6.2" fill="none" stroke="#6f6cb2" stroke-width="1.8"/></svg><span>Body Sculpting/<br>Contouring</span></div>
    <div class="service s-maint"><svg width="18" height="18" viewBox="0 0 18 18"><circle cx="9" cy="9" r="7.5" fill="none" stroke="#6f6cb2" stroke-width="1.6"/><path d="M5.5 9.2 L8 11.6 L13 6.2" fill="none" stroke="#6f6cb2" stroke-width="1.8"/></svg><span>Maintenance<br>&amp; Recovery<br>Program</span></div>
    <div class="service s-cavit"><svg width="18" height="18" viewBox="0 0 18 18"><circle cx="9" cy="9" r="7.5" fill="none" stroke="#6f6cb2" stroke-width="1.6"/><path d="M5.5 9.2 L8 11.6 L13 6.2" fill="none" stroke="#6f6cb2" stroke-width="1.8"/></svg><span>Cavitation</span></div>
    <div class="service s-facial"><svg width="18" height="18" viewBox="0 0 18 18"><circle cx="9" cy="9" r="7.5" fill="none" stroke="#6f6cb2" stroke-width="1.6"/><path d="M5.5 9.2 L8 11.6 L13 6.2" fill="none" stroke="#6f6cb2" stroke-width="1.8"/></svg><span>Facials</span></div>
    <div class="service s-detox"><svg width="18" height="18" viewBox="0 0 18 18"><circle cx="9" cy="9" r="7.5" fill="none" stroke="#6f6cb2" stroke-width="1.6"/><path d="M5.5 9.2 L8 11.6 L13 6.2" fill="none" stroke="#6f6cb2" stroke-width="1.8"/></svg><span>Detoxing</span></div>

    <div class="brand-dot"></div>
    <h1 class="brand-name">SILVER REED</h1>
    <p class="tagline">WHERE BEAUTY AND WELLNESS FIND HARMONY</p>

    <div class="phone">
      <svg width="34" height="38" viewBox="0 0 24 26" aria-hidden="true">
        <path d="M5 2 C3 3 2 5 2.5 8 C4 15 9 21 15 24 C18 25 20 24 21 22 L18 18 C17 17 16 17 15 18 L13.5 19 C10 17 8 13 7 10 L8.5 9 C9.5 8 9.5 7 9 6 Z" fill="#1b1b1b"/>
        <path d="M14 5 A6 6 0 0 1 19 10 M14 1.5 A9.5 9.5 0 0 1 22.5 10" fill="none" stroke="#1b1b1b" stroke-width="1.6"/>
      </svg>
      <span>123.456.7890</span>
    </div>
    <p class="web">WWW.<span class="domain">SILVERREED</span>.COM</p>
    <p class="email">HELLO@SILVERREED.COM</p>
  </section>

</main>
</body>
</html>
```